Science News Webpage Design

Quarry Lantern Works gGmbH is a non-profit organisation developing apps for scientists. Our main project is a scientific platform you can visit at quarrylantern.net.

The QLW platform consists of multiple modules. We are now considering to spin out one of the modules (Tides & Notes) and create a separate web application with focus on latest science news that enables scientists to easily contribute by writing their own articles and commentaries.

For this news website, we need someone to design the homepage and three other templates.

We prepared a set of files consisting of a more detailed brief and also a couple of wire-frames.

Please check these files and get in touch with us in case you have questions or in case something is unclear.
Updates

Hello everyone,

Just a short note. Although I have indicated in the brief that this project is a spin-out from another platform, you shouldn't feel restricted to design and color combinations of that other site. We are really trying to make something new here, and the design can be completely different.

I also attached a new file. The working title of the project is "wonder unwrapped". Although we haven't decided on the final name, you can use this png as logo.

Cheers,
Toma

Updated home page wireframe to include all links in the menu (since there are more links than originally depicted and this obviously influences design).

Industry/Entity Type

Non-Profit

```html
<!DOCTYPE html>
<html lang="en">
<head>
<meta charset="utf-8">
<title>Quarry Lantern Works – Science, health and technology news</title>
<link href="https://fonts.googleapis.com/css2?family=Open+Sans:ital,wdth,wght@0,75..100,300..800;1,75..100,300..800&family=Crimson+Text:ital,wght@1,400;1,600&display=swap" rel="stylesheet">
<style>
:root{
  --red:#e8402f;
  --ink:#222;
  --text:#5a5a5a;
  --muted:#8a8a8a;
  --page:#f2f2f4;
  --grid:#e8e8ec;
  --rule:#d9d9dd;
  --white:#fff;
  --ad-blue:#1d3f78;
  --ad-yellow:#f6c416;
  --soc-a:#3b5998;
  --soc-b:#2aa3e0;
  --soc-c:#d9312b;
  --soc-d:#34465d;
}
*{box-sizing:border-box;margin:0;padding:0}
html,body{width:1200px;height:2428px;overflow:hidden}
body{
  position:relative;
  font-family:"Open Sans",Arial,sans-serif;
  font-stretch:87.5%;
  color:var(--ink);
  background-color:var(--page);
  background-image:
    repeating-linear-gradient(0deg,var(--grid) 0 1px,transparent 1px 12px),
    repeating-linear-gradient(90deg,var(--grid) 0 1px,transparent 1px 12px);
}
a{color:inherit;text-decoration:none}

/* promo strip */
.promo-strip{position:absolute;left:0;top:0;width:1200px;height:113px;background:var(--white)}
.promo{
  position:absolute;left:318px;top:24px;width:566px;height:69px;
  background:var(--ad-blue);color:var(--white);
  padding:13px 16px;font-size:15px;line-height:20px;letter-spacing:.2px;white-space:nowrap;
}
.promo strong{color:var(--ad-yellow);font-weight:700}
.promo .cta{text-decoration:underline;font-weight:600}
.promo-badge{position:absolute;left:412px;top:10px;width:142px;height:49px;background:var(--ad-yellow);border-radius:4px}

/* masthead */
.masthead{position:absolute;left:0;top:113px;width:1200px;height:112px;background:linear-gradient(#1a1a1a,#050505)}
.brand{position:absolute;left:134px;top:20px;display:flex;align-items:center;gap:10px}
.brand-dot{width:32px;height:32px;border-radius:50%;background:var(--red)}
.brand-name{color:var(--white);font-weight:700;font-size:19px;line-height:21px;white-space:nowrap}
.beta{position:absolute;left:242px;top:48px;color:var(--white);font-size:10px;font-weight:600}
.brand-tag{position:absolute;left:134px;top:80px;color:var(--white);font-size:11px;font-weight:700;white-space:nowrap}
.main-nav{position:absolute;left:376px;top:50px;color:var(--red);font-size:11.5px;font-weight:400;white-space:nowrap;font-stretch:80%}
.main-nav a{margin-right:2px}
.account{
  position:absolute;left:917px;top:-8px;width:142px;height:41px;
  background:var(--red);border-radius:0 0 6px 6px;
  display:flex;align-items:center;justify-content:center;
  color:var(--white);font-size:12px;font-weight:700;white-space:nowrap;
}
.account a{padding:0 12px}
.account a+a{border-left:1px solid rgba(255,255,255,.5)}
.follow{position:absolute;color:var(--white);font-size:11px;font-weight:700;white-space:nowrap}
.masthead .follow{left:884px;top:47px}
.social{position:absolute;display:flex}
.masthead .social{left:884px;top:65px;gap:12px}
.social span{display:block;border-radius:5px}
.masthead .social span{width:36px;height:36px}
.social .s1{background:var(--soc-a)}
.social .s2{background:var(--soc-b)}
.social .s3{background:var(--soc-c)}
.social .s4{background:var(--soc-d)}

/* shared */
.block{position:absolute}
.section-head{
  display:flex;justify-content:space-between;align-items:flex-end;
  border-bottom:2px solid var(--red);height:20px;padding-bottom:2px;margin-bottom:8px;
}
.section-head h2{color:var(--red);font-size:13px;font-weight:400;text-transform:uppercase;letter-spacing:.3px}
.section-head a{font-size:11px;font-weight:700;color:var(--ink)}
.photo{display:block;width:100%;height:180px}
.headline{color:var(--red);font-size:14px;line-height:19px;margin:8px 0 4px;font-weight:400}
.meta{font-family:"Crimson Text",Georgia,serif;font-style:italic;font-size:12px;color:var(--ink);line-height:16px}
.meta .sep{margin:0 12px}
.excerpt{font-size:12px;line-height:16px;color:var(--text);margin-top:5px}
.card{padding-bottom:14px;border-bottom:1px solid var(--rule);margin-bottom:14px}
.more{
  display:block;width:82px;height:22px;
  background:var(--red);color:var(--white);border-radius:3px;
  font-size:10px;font-weight:800;text-align:center;line-height:22px;letter-spacing:.3px;
}
.more.placed{position:absolute}
.col{position:absolute;top:0;width:290px}
.c1{left:0}.c2{left:317px}.c3{left:641px;width:292px}

/* compact list */
.mini{display:flex;gap:8px}
.mini .thumb{flex:0 0 105px;height:75px}
.mini h3,.stacked h3{color:var(--red);font-size:12px;line-height:14px;font-weight:400}
.mini p,.stacked p{font-size:10.5px;line-height:13px;color:var(--text);margin-top:3px}
.mini-meta{font-family:"Crimson Text",Georgia,serif;font-style:italic;font-size:11px;line-height:14px;margin-top:4px}
.mini-meta .sep{margin:0 10px}
.item{padding-bottom:6px;border-bottom:1px solid var(--rule);margin-bottom:8px}

/* sidebar */
.search{height:46px;background:#dcdcde;border-radius:3px;padding:10px 8px;display:flex;gap:14px}
.search-field{flex:1;background:var(--white);border-radius:13px;height:26px;font-size:11px;color:var(--muted);padding:5px 12px;position:relative}
.search-field svg{position:absolute;right:10px;top:7px}
.search .more{margin-top:2px}
.signup{text-align:center;margin-top:16px}
.signup h2{color:var(--red);font-size:26px;font-weight:400;line-height:32px}
.signup p{font-size:14px;color:var(--text);line-height:18px}
.signup a{display:inline-block;margin-top:10px;color:var(--red);font-size:14px;text-decoration:underline}

/* sponsored */
.sponsored{position:absolute;left:0;top:1155px;width:1200px;height:306px;background:linear-gradient(#0c0c0c,#161616 50%,#0a0a0a)}
.sponsored h2{position:absolute;left:134px;top:20px;color:var(--red);font-size:21px;font-weight:400;letter-spacing:.3px}
.sponsor-card{position:absolute;top:53px;width:203px}
.sponsor-card .thumb{height:144px}
.sponsor-card p{color:#8b8b8b;font-size:10.5px;line-height:14px;margin-top:16px}
.sponsor-card .meta{color:var(--white);font-size:11.5px;margin-top:8px}

/* ads */
.book-ad{height:193px;background:#e4e4e4;border:1px solid #cfcfcf;display:flex;gap:8px;padding:8px;margin-left:28px;width:233px}
.book-cover{flex:0 0 88px;height:175px}
.book-copy{font-family:"Crimson Text",Georgia,serif;color:#111;font-weight:600;font-size:16px;line-height:17px;text-align:center;padding-top:4px}
.book-copy small{display:block;margin-top:10px;font-size:13px;line-height:15px}
.label{color:var(--red);font-size:13px;text-transform:uppercase;margin:48px 0 10px}

/* footer */
.site-footer{position:absolute;left:0;top:2362px;width:1200px;height:66px;background:var(--red)}
.footer-links{position:absolute;left:134px;top:25px;color:var(--white);font-size:11px;white-space:nowrap}
.footer-links a{margin-right:3px}
.site-footer .follow{left:770px;top:25px}
.site-footer .social{left:852px;top:13px;gap:18px}
.site-footer .social span{width:40px;height:40px}
</style>
</head>
<body>

<div class="promo-strip">
  <div class="promo">
    <div>JOIN <strong>QUAKEREADY</strong> OUR NATIONAL EARTHQUAKE DRILL, SEPT 26</div>
    <div class="cta">SIGN UP NOW</div>
    <span class="promo-badge" role="img" aria-label="Drill partner badge"></span>
  </div>
</div>

<header class="masthead">
  <div class="brand"><span class="brand-dot"></span><span class="brand-name">Quarry Lantern<br>Works</span></div>
  <span class="beta">BETA</span>
  <div class="brand-tag">Science, health and technology news</div>
  <nav class="main-nav">
    <a href="#">LATEST</a> <a href="#">BIOLOGY</a> <a href="#">CHEMISTRY</a> <a href="#">PHYSICS</a> <a href="#">COMPUTATION</a> <a href="#">TECHNOLOGY</a> <a href="#">HEALTH</a> <a href="#">QUESTIONS?</a>
  </nav>
  <div class="account"><a href="#">Sign in</a><a href="#">Sign up</a></div>
  <div class="follow">Follow us</div>
  <div class="social"><span class="s1" role="img" aria-label="Social link"></span><span class="s2" role="img" aria-label="Social link"></span><span class="s3" role="img" aria-label="Video channel link"></span><span class="s4" role="img" aria-label="Blog link"></span></div>
</header>

<!-- latest -->
<section class="block" style="left:134px;top:243px;width:613px;height:360px">
  <div class="section-head"><h2>Latest</h2><a href="#">See all</a></div>
  <div class="col c1" style="top:30px">
    <div class="photo" role="img" aria-label="Glowing green laser diode on a circuit" style="height:182px;background:radial-gradient(circle at 50% 45%,#b9ff9a 0,#39c24a 12%,#1f4a32 45%,#14221c 100%)"></div>
    <h3 class="headline">Lorem ipsum dolor sit amet, conse ctetur adipiscing elit. Aliquam leo nisl, tincidunt</h3>
    <div class="meta">Genetic engineering<span class="sep">|</span>Article by: J. Smith</div>
    <p class="excerpt">Lorem ipsum dolor sit amet, consectetur adipiscing elit. Aliquam leo nisl, tincidunt et dolor eu, euismod placerat sapien.</p>
  </div>
  <a class="more placed" href="#" style="left:206px;top:328px">READ MORE</a>
  <div class="col c2" style="top:30px">
    <div class="item">
      <div class="mini">
        <div class="thumb" role="img" aria-label="Diagram of particle interactions" style="background:linear-gradient(#fafafa,#e9e6ee)"></div>
        <div><h3>Lorem ipsum dolor sit amet, conse ctetur adipiscing elit.</h3><p>Lorem ipsum dolor sit amet, con sectetur adipiscing elit. Aliquam leo nisl, tincidunt et dolor eu, euismod</p></div>
      </div>
      <div class="mini-meta">Genetic engineering<span class="sep">|</span>Article by: J. Smith</div>
    </div>
    <div class="item">
      <div class="mini">
        <div class="thumb" role="img" aria-label="Glowing red crystal on black" style="background:radial-gradient(circle,#ff5a2a 0,#a3150d 40%,#150404 80%)"></div>
        <div><h3>Lorem ipsum dolor sit amet, conse ctetur adipiscing elit.</h3><p>Lorem ipsum dolor sit amet, con sectetur adipiscing elit. Aliquam leo nisl, tincidunt et dolor eu, euismod</p></div>
      </div>
      <div class="mini-meta">Genetic engineering<span class="sep">|</span>Article by: J. Smith</div>
    </div>
    <div class="stacked">
      <h3>Lorem ipsum dolor sit amet, consectetur adipiscing elit. Aliquam leo nisl, tincidunt et dolor eu.</h3>
      <p>Lorem ipsum dolor sit amet, consectetur adipiscing elit. Aliquam leo nisl, tincidunt et dolor eu, euismod placerat sa pien. Vivamus tristique pretium sodales. Praesent ante</p>
      <div class="mini-meta">Genetic engineering<span class="sep">|</span>Article by: J. Smith</div>
    </div>
  </div>
</section>

<aside class="block" style="left:775px;top:243px;width:292px">
  <div class="search">
    <div class="search-field">search
      <svg width="12" height="12" viewBox="0 0 12 12"><circle cx="5" cy="5" r="3.6" fill="none" stroke="#888" stroke-width="1.5"/><line x1="7.6" y1="7.6" x2="11" y2="11" stroke="#888" stroke-width="1.5"/></svg>
    </div>
    <a class="more" href="#">READ MORE</a>
  </div>
  <div class="signup">
    <h2>Sign up</h2>
    <p>to upload articles, bookmark,<br>comment...</p>
    <a href="#">Find out more</a>
  </div>
  <div role="img" aria-label="Space-themed poster advertisement" style="margin:18px 0 0 30px;width:231px;height:194px;background:radial-gradient(circle at 60% 40%,#3a3f56 0,#14172a 55%,#05060c 100%)"></div>
</aside>

<!-- row 2 -->
<section class="block" style="left:134px;top:623px;width:933px;height:510px">
  <div class="col c1">
    <div class="section-head"><h2>Biology</h2><a href="#">See all</a></div>
    <div class="card">
      <div class="photo" role="img" aria-label="DNA double helix model" style="background:linear-gradient(135deg,#dfe9f2,#a9c4dc 55%,#e7eef5)"></div>
      <h3 class="headline">Lorem ipsum dolor sit amet, conse ctetur adipiscing elit. Aliquam leo nisl, tincidunt</h3>
      <div class="meta">Genetic engineering<span class="sep">|</span>Article by: J. Smith</div>
      <p class="excerpt">Lorem ipsum dolor sit amet, consectetur adipiscing elit. Aliquam leo nisl, tincidunt et dolor eu, euismod placerat sapien.</p>
    </div>
    <h3 class="headline" style="margin-top:0">Lorem ipsum dolor sit amet, conse ctetur adipiscing elit. Aliquam leo nisl, tincidunt</h3>
    <div class="meta">Genetic engineering<span class="sep">|</span>Article by: J. Smith</div>
    <p class="excerpt">Lorem ipsum dolor sit amet, consectetur adipiscing elit. Aliquam leo nisl, tincidunt et dolor eu, euismod placerat sapien.</p>
  </div>
  <a class="more placed" href="#" style="left:104px;top:482px">READ MORE</a>
  <div class="col c2">
    <div class="section-head"><h2>Chemistry</h2><a href="#">See all</a></div>
    <div class="card">
      <div class="photo" role="img" aria-label="Laboratory flasks with pink liquid" style="background:linear-gradient(160deg,#eef0f4,#c9cfdc 45%,#d58ad4 75%,#e6e0ea)"></div>
      <h3 class="headline">Lorem ipsum dolor sit amet, conse ctetur adipiscing elit. Aliquam leo nisl, tincidunt</h3>
      <div class="meta">Genetic engineering<span class="sep">|</span>Article by: J. Smith</div>
      <p class="excerpt">Lorem ipsum dolor sit amet, consectetur adipiscing elit. Aliquam leo nisl, tincidunt et dolor eu, euismod placerat sapien.</p>
    </div>
    <h3 class="headline" style="margin-top:0">Lorem ipsum dolor sit amet, conse ctetur adipiscing elit. Aliquam leo nisl, tincidunt</h3>
    <div class="meta">Genetic engineering<span class="sep">|</span>Article by: J. Smith</div>
    <p class="excerpt">Lorem ipsum dolor sit amet, consectetur adipiscing elit. Aliquam leo nisl, tincidunt et dolor eu, euismod placerat sapien.</p>
  </div>
  <a class="more placed" href="#" style="left:421px;top:482px">READ MORE</a>
  <div class="col c3">
    <div class="section-head"><h2>Most popular</h2><a href="#">See all</a></div>
    <div class="item">
      <div class="mini">
        <div class="thumb" role="img" aria-label="Green laser diode" style="background:radial-gradient(circle,#9cf58a 0,#2d8c3c 25%,#17301f 80%)"></div>
        <div><h3>Lorem ipsum dolor sit amet, conse ctetur adipiscing elit.</h3><p>Lorem ipsum dolor sit amet, con sectetur adipiscing elit. Aliquam leo nisl, tincidunt et dolor eu, euismod</p></div>
      </div>
      <div class="mini-meta">Genetic engineering<span class="sep">|</span>Article by: J. Smith</div>
    </div>
    <div class="item">
      <div class="mini">
        <div class="thumb" role="img" aria-label="Green laser diode" style="background:radial-gradient(circle,#9cf58a 0,#2d8c3c 25%,#17301f 80%)"></div>
        <div><h3>Lorem ipsum dolor sit amet, conse ctetur adipiscing elit.</h3><p>Lorem ipsum dolor sit amet, con sectetur adipiscing elit. Aliquam leo nisl, tincidunt et dolor eu, euismod</p></div>
      </div>
      <div class="mini-meta">Genetic engineering<span class="sep">|</span>Article by: J. Smith</div>
    </div>
    <div class="item stacked">
      <h3>Lorem ipsum dolor sit amet, consectetur adipiscing elit. Aliquam leo nisl, tincidunt et dolor eu.</h3>
      <p>Lorem ipsum dolor sit amet, con sectetur adipiscing elit. Aliquam leo nisl, tincidunt et dolor eu, euismod placerat sapien. Vivamus tristique pretium sodales.</p>
      <div class="mini-meta">Genetic engineering<span class="sep">|</span>Article by: J. Smith</div>
    </div>
    <div class="item">
      <div class="mini">
        <div class="thumb" role="img" aria-label="Green laser diode" style="background:radial-gradient(circle,#9cf58a 0,#2d8c3c 25%,#17301f 80%)"></div>
        <div><h3>Lorem ipsum dolor sit amet, conse ctetur adipiscing elit.</h3><p>Lorem ipsum dolor sit amet, con sectetur adipiscing elit. Aliquam leo nisl, tincidunt et dolor eu, euismod</p></div>
      </div>
      <div class="mini-meta">Genetic engineering<span class="sep">|</span>Article by: J. Smith</div>
    </div>
  </div>
  <a class="more placed" href="#" style="left:746px;top:482px">READ MORE</a>
</section>

<!-- sponsored -->
<section class="sponsored">
  <h2>SPONSORED</h2>
  <div class="sponsor-card" style="left:134px">
    <div class="thumb" role="img" aria-label="Laboratory glassware with pink solution" style="background:linear-gradient(160deg,#e9edf3,#b8c2d4 50%,#d47fd0 80%)"></div>
    <p>Morbi tortor erat, euismod interdum rhoncus ac, tempus non massa. Proin in lectus varius neque bibendum bibendum</p>
    <div class="meta">Genetic engineering<span class="sep">|</span>Article by: J. Smith</div>
  </div>
  <div class="sponsor-card" style="left:376px">
    <div class="thumb" role="img" aria-label="Spheres in a glowing blue tunnel" style="background:radial-gradient(circle at 50% 50%,#e6f6ff 0,#4aa2df 30%,#0c2a4e 85%)"></div>
    <p>Morbi tortor erat, euismod interdum rhoncus ac, tempus non massa. Proin in lectus varius neque bibendum bibendum</p>
    <div class="meta">Genetic engineering<span class="sep">|</span>Article by: J. Smith</div>
  </div>
  <div class="sponsor-card" style="left:621px">
    <div class="thumb" role="img" aria-label="Gloved hands holding a seedling sample" style="background:linear-gradient(150deg,#2a3f74,#7b90c4 50%,#c5d0ea)"></div>
    <p>Morbi tortor erat, euismod interdum rhoncus ac, tempus non massa. Proin in lectus varius neque bibendum bibendum</p>
    <div class="meta">Genetic engineering<span class="sep">|</span>Article by: J. Smith</div>
  </div>
  <div class="sponsor-card" style="left:864px">
    <div class="thumb" role="img" aria-label="Blue glowing circuit board" style="background:linear-gradient(135deg,#0a3a75,#19a4e6 50%,#0b2d5c)"></div>
    <p>Morbi tortor erat, euismod interdum rhoncus ac, tempus non massa. Proin in lectus varius neque bibendum bibendum</p>
    <div class="meta">Genetic engineering<span class="sep">|</span>Article by: J. Smith</div>
  </div>
</section>

<!-- row 3 -->
<section class="block" style="left:134px;top:1489px;width:933px;height:510px">
  <div class="col c1">
    <div class="section-head"><h2>Physics</h2><a href="#">See all</a></div>
    <div class="card">
      <div class="photo" role="img" aria-label="Pink plasma discharge" style="background:radial-gradient(circle at 50% 55%,#ffd6f2 0,#e0389c 25%,#7a0f4c 60%,#250511 100%)"></div>
      <h3 class="headline">Lorem ipsum dolor sit amet, conse ctetur adipiscing elit. Aliquam leo nisl, tincidunt</h3>
      <div class="meta">Genetic engineering<span class="sep">|</span>Article by: J. Smith</div>
      <p class="excerpt">Lorem ipsum dolor sit amet, consectetur adipiscing elit. Aliquam leo nisl, tincidunt et dolor eu, euismod placerat sapien.</p>
    </div>
    <h3 class="headline" style="margin-top:0">Lorem ipsum dolor sit amet, conse ctetur adipiscing elit. Aliquam leo nisl, tincidunt</h3>
    <div class="meta">Genetic engineering<span class="sep">|</span>Article by: J. Smith</div>
    <p class="excerpt">Lorem ipsum dolor sit amet, consectetur adipiscing elit. Aliquam leo nisl, tincidunt et dolor eu, euismod placerat sapien.</p>
  </div>
  <a class="more placed" href="#" style="left:104px;top:482px">READ MORE</a>
  <div class="col c2">
    <div class="section-head"><h2>Computation</h2><a href="#">See all</a></div>
    <div class="card">
      <div class="photo" role="img" aria-label="Digital globe against a cloudy sky" style="background:linear-gradient(#5fa3de,#bcd9f1 55%,#f2f6fa)"></div>
      <h3 class="headline">Lorem ipsum dolor sit amet, conse ctetur adipiscing elit. Aliquam leo nisl, tincidunt</h3>
      <div class="meta">Genetic engineering<span class="sep">|</span>Article by: J. Smith</div>
      <p class="excerpt">Lorem ipsum dolor sit amet, consectetur adipiscing elit. Aliquam leo nisl, tincidunt et dolor eu, euismod placerat sapien.</p>
    </div>
    <h3 class="headline" style="margin-top:0">Lorem ipsum dolor sit amet, conse ctetur adipiscing elit. Aliquam leo nisl, tincidunt</h3>
    <div class="meta">Genetic engineering<span class="sep">|</span>Article by: J. Smith</div>
    <p class="excerpt">Lorem ipsum dolor sit amet, consectetur adipiscing elit. Aliquam leo nisl, tincidunt et dolor eu, euismod placerat sapien.</p>
  </div>
  <a class="more placed" href="#" style="left:421px;top:482px">READ MORE</a>
  <div class="col c3" style="top:6px">
    <div class="book-ad">
      <div class="book-cover" role="img" aria-label="Novel cover with a close-up eye" style="background:linear-gradient(#f4f4f4 0 22%,#3b4a5a 22% 70%,#efefef 70%)"></div>
      <div class="book-copy">Escape to a Future from which there is No Return<small>Harbor by<br>Milo Varga<br>E-book</small></div>
    </div>
    <div class="label">Visit also</div>
    <div role="img" aria-label="Spheres in a glowing blue tunnel" style="margin-left:28px;width:233px;height:192px;background:radial-gradient(circle at 50% 50%,#e6f6ff 0,#4aa2df 30%,#0c2a4e 85%)"></div>
  </div>
</section>

<!-- row 4 -->
<section class="block" style="left:134px;top:2012px;width:933px;height:340px">
  <div class="col c1">
    <div class="section-head"><h2>Technology</h2><a href="#">See all</a></div>
    <div class="photo" role="img" aria-label="Laptop with app icons bursting out" style="background:linear-gradient(160deg,#f2f2f2,#9aa3ad 55%,#2f3338)"></div>
    <h3 class="headline">Lorem ipsum dolor sit amet, conse ctetur adipiscing elit. Aliquam leo nisl, tincidunt</h3>
    <div class="meta">Genetic engineering<span class="sep">|</span>Article by: J. Smith</div>
    <p class="excerpt">Lorem ipsum dolor sit amet, consectetur adipiscing elit. Aliquam leo nisl, tincidunt et dolor eu, euismod placerat sapien.</p>
  </div>
  <div class="col c2">
    <div class="section-head"><h2>Health</h2><a href="#">See all</a></div>
    <div class="photo" role="img" aria-label="Stethoscope and pills on a blue chart" style="background:linear-gradient(135deg,#2f5f93,#7fa6cf 50%,#dfe7f1)"></div>
    <h3 class="headline">Lorem ipsum dolor sit amet, conse ctetur adipiscing elit. Aliquam leo nisl, tincidunt</h3>
    <div class="meta">Genetic engineering<span class="sep">|</span>Article by: J. Smith</div>
    <p class="excerpt">Lorem ipsum dolor sit amet, consectetur adipiscing elit. Aliquam leo nisl, tincidunt et dolor eu, euismod placerat sapien.</p>
  </div>
  <div class="col c3">
    <div class="section-head"><h2>Other</h2><a href="#">See all</a></div>
    <div class="photo" role="img" aria-label="Grey molecular network graphic" style="background:linear-gradient(135deg,#ffffff,#d6d6d6 60%,#f4f4f4)"></div>
    <h3 class="headline">Lorem ipsum dolor sit amet, conse ctetur adipiscing elit. Aliquam leo nisl, tincidunt</h3>
    <div class="meta">Genetic engineering<span class="sep">|</span>Article by: J. Smith</div>
    <p class="excerpt">Lorem ipsum dolor sit amet, consectetur adipiscing elit. Aliquam leo nisl, tincidunt et dolor eu, euismod placerat sapien.</p>
  </div>
</section>

<footer class="site-footer">
  <nav class="footer-links"><a href="#">About QLW</a> <a href="#">Terms of use</a> <a href="#">Privacy policy</a> <a href="#">For Advertisers</a> <a href="#">Contact us</a> <a href="#">Feedback</a> <a href="#">Help</a></nav>
  <div class="follow">Follow us</div>
  <div class="social"><span class="s1" role="img" aria-label="Social link"></span><span class="s2" role="img" aria-label="Social link"></span><span class="s3" role="img" aria-label="Video channel link"></span><span class="s4" role="img" aria-label="Blog link"></span></div>
</footer>

</body>
</html>
```